I need a great, modern, professional website for my paint contracting company, Brookhollow Paint Contractors, LLC. I have many good pix that can be used from jobs completed that would be attractive. We do commercial, residential and industrial jobs. I’m fully insured and licensed, including holding a General Contractor’s License as a Subcontractor. I know nothing about coding websites. I’ll have my assistant get on tomorrow and learn how to drop files. I’m not sure what files to send. This will be difficult at best, it being able to talk this through. Oh well. What’s next?

Target Market(s)

General Contractors

Industry/Entity Type

Paint Contracting

Coding

Coded - Design and coding required

Font styles to use
Sans Serif

Colors
00AB8E
00BBA5
67D7C9
C6EFE9
E9F9F6

Requirements
Must have
• Pix of completed jobs, bio, maybe testimonials from happy customers? ….
Nice to have
• I’d like it to have a modern appeal, but still have some warmth.
Should not have
• ??

```html
<!DOCTYPE html>
<html lang="en">
<head>
<meta charset="utf-8">
<title>Brookhollow Paint Contractors, LLC</title>
<link href="https://fonts.googleapis.com/css2?family=Bebas+Neue&family=Source+Sans+3:wght@400;600;700&display=swap" rel="stylesheet">
<style>
:root{
  --green:#00AB8E;
  --green-2:#00BBA5;
  --green-3:#67D7C9;
  --mint:#C6EFE9;
  --mint-pale:#E9F9F6;
  --ink:#222;
  --text:#333;
  --muted:#666;
  --dark:#2b2b2b;
  --topbar:#2e2e2e;
  --teal-deep:#0d5a5a;
  --star:#f5b800;
}
*{box-sizing:border-box;margin:0;padding:0}
html,body{width:1200px;height:2492px;overflow:hidden}
body{position:relative;background:#fff;font-family:"Source Sans 3",Arial,sans-serif;color:var(--text)}
.abs{position:absolute}
.display{font-family:"Bebas Neue",Impact,sans-serif;font-weight:400;letter-spacing:2px;color:var(--ink)}
.btn{position:absolute;background:var(--green);color:#fff;font-weight:700;font-size:10px;letter-spacing:.2px;display:flex;align-items:center;justify-content:center;text-transform:uppercase}

/* header */
.topbar{left:320px;top:0;width:880px;height:29px;background:var(--topbar);color:#fff;font-size:10px}
.topbar .item{position:absolute;top:0;height:29px;display:flex;align-items:center;gap:6px}
.topbar .divider{position:absolute;left:636px;top:4px;width:1px;height:22px;background:#666}
.social-dot{position:absolute;top:7px;width:15px;height:15px;border-radius:50%;background:var(--green-2)}
.brand{left:113px;top:18px;font-size:30px;font-weight:700;color:var(--green-3);letter-spacing:1px}
.nav{top:46px;left:528px;display:flex;gap:31px;font-size:9.5px;color:#333}
.nav .active{color:var(--green);font-weight:700}

/* hero */
.hero-photo{left:0;top:75px;width:1200px;height:531px;background:linear-gradient(100deg,#0b4f52 0%,#0f6a6b 45%,#0a5a5d 70%,#063c3f 100%)}
.hero-title{left:113px;top:212px;font-size:51px;line-height:50px;color:#fff;letter-spacing:3px}
.hero-sub{left:113px;top:374px;font-size:17px;color:#fff}

/* consultation */
.section-title{width:1200px;left:0;text-align:center}
.consult-lead{left:0;width:1200px;top:672px;text-align:center;font-size:12.5px;color:#333}
.step{top:716px;display:flex;align-items:flex-start;gap:6px}
.step .num{font-size:58px;line-height:56px;color:#c9c9c9;font-weight:400}
.step .small{font-size:14px;color:#333;margin-top:6px}
.step .big{font-size:31px;line-height:30px;color:var(--green-2)}
.field{top:806px;width:200px;border-bottom:1px solid #bbb;font-size:12.5px;padding-bottom:14px;color:#333}

/* trusted */
.trusted-photo{left:600px;top:934px;width:600px;height:324px;background:linear-gradient(90deg,#ffffff 0%,#e8ecec 10%,#0e6b6b 30%,#0e6b6b 70%,#c9a77a 100%)}
.body-copy{font-size:12.5px;line-height:18.7px;color:#333}

/* reviews */
.reviews{left:0;top:1258px;width:1200px;height:397px;background:var(--mint-pale)}
.card{top:1348px;width:315px;height:224px;border:1px solid #d3ece7;background:var(--mint-pale);padding:0 18px}
.avatar{position:absolute;left:18px;top:25px;width:50px;height:50px;border-radius:50%;background:linear-gradient(#dcdcdc,#8b8f96)}
.reviewer{position:absolute;left:87px;top:34px;font-family:"Bebas Neue",Impact,sans-serif;font-size:17px;letter-spacing:1px;color:#333}
.stars{position:absolute;left:87px;top:56px}
.review-text{position:absolute;left:18px;right:14px;top:92px;font-size:12.5px;line-height:18.7px;color:#333}

/* projects */
.pattern-band{left:0;top:1776px;width:1200px;height:286px;background:linear-gradient(90deg,#0f4a3f,#1e6b55 20%,#123f38 50%,#1e6b55 80%,#0f4a3f)}
.project{top:1738px;width:417px;height:363px;background:#fff;box-shadow:0 2px 8px rgba(0,0,0,.12)}
.project .photo{position:absolute;left:5px;top:5px;width:407px;height:281px}
.project h3{position:absolute;left:37px;top:302px;font-family:"Bebas Neue",Impact,sans-serif;font-weight:400;font-size:20px;letter-spacing:1.5px;color:var(--green)}
.project p{position:absolute;left:37px;top:327px;font-size:12.5px;color:#333}

/* newsletter */
.newsletter{left:0;top:2187px;width:1200px;height:168px;background:linear-gradient(90deg,var(--green-3) 0%,#3cc6b0 55%,var(--green) 100%)}

/* footer */
.footer{left:0;top:2355px;width:1200px;height:137px;background:var(--dark);color:#fff}
.footer h4{font-size:12px;font-weight:700;letter-spacing:.4px;margin-bottom:6px}
.footer li{list-style:none;font-size:9.5px;line-height:15.5px}
.footer-dot{position:absolute;top:52px;width:26px;height:26px;border-radius:50%;background:var(--green-2)}
</style>
</head>
<body>

<!-- Header -->
<div class="abs brand">Brookhollow</div>
<div class="abs topbar">
  <div class="item" style="left:208px">
    <svg width="20" height="14" viewBox="0 0 20 14"><rect x="0.5" y="0.5" width="19" height="13" fill="#1fb39a"/><path d="M1 1 L10 8 L19 1" fill="none" stroke="#2e2e2e" stroke-width="1.4"/></svg>
    <span>brookhollowpaint@mailbox.co.nz</span>
  </div>
  <div class="item" style="left:430px">
    <svg width="17" height="17" viewBox="0 0 24 24"><path fill="#1fb39a" d="M6.6 10.8a15.1 15.1 0 0 0 6.6 6.6l2.2-2.2a1 1 0 0 1 1-.25 11.4 11.4 0 0 0 3.6.57 1 1 0 0 1 1 1V20a1 1 0 0 1-1 1A17 17 0 0 1 3 4a1 1 0 0 1 1-1h3.5a1 1 0 0 1 1 1c0 1.25.2 2.45.57 3.57a1 1 0 0 1-.25 1z"/></svg>
    <span>Call us today on - 0271458830</span>
  </div>
  <div class="divider"></div>
  <span class="social-dot" style="left:681px" role="img" aria-label="Social profile"></span>
  <span class="social-dot" style="left:713px" role="img" aria-label="Social profile"></span>
  <span class="social-dot" style="left:751px" role="img" aria-label="Social profile"></span>
</div>
<nav class="abs nav">
  <span class="active">HOME</span><span>ABOUT US</span><span>OUR SERVICES</span><span>OUR PROJECTS</span><span>CONTACT</span>
</nav>
<div class="btn" style="left:950px;top:38px;width:138px;height:29px">Request a free quote</div>

<!-- Hero -->
<div class="abs hero-photo" role="img" aria-label="Teal panelled living room with velvet armchair and black floor lamp"></div>
<h1 class="abs display hero-title">For all your house<br>painting needs in West<br>Auckland and Auckland wide.</h1>
<p class="abs hero-sub">If you need painting in Auckland, whatever size of project, contact us today</p>
<div class="btn" style="left:113px;top:409px;width:137px;height:28px">Request a free quote</div>

<!-- Free consultation -->
<h2 class="abs display section-title" style="top:626px;font-size:40px">Free Consultation</h2>
<p class="abs consult-lead">Allow our Coastline Paints experts answer your queries regarding colour preferences, combinations, durability and anything that would enhance the beauty of your home</p>
<div class="abs step" style="left:170px"><span class="num">1</span><div><div class="small">What type of</div><div class="big">Paint?</div></div></div>
<div class="abs step" style="left:469px"><span class="num">2</span><div><div class="small">What type of</div><div class="big">Colour?</div></div></div>
<div class="abs step" style="left:791px"><span class="num">3</span><div><div class="small">What type of</div><div class="big">Long Lasting?</div></div></div>
<div class="abs field" style="left:143px">Name</div>
<div class="abs field" style="left:381px">Email</div>
<div class="abs field" style="left:619px">Mobile No</div>
<div class="abs field" style="left:857px">Pincode</div>
<div class="btn" style="left:525px;top:869px;width:150px;height:29px">Get a free consultancy</div>

<!-- Trusted painters -->
<div class="abs trusted-photo" role="img" aria-label="Smiling painter in hard hat holding a brush beside a teal room with armchair and shelving"></div>
<h2 class="abs display" style="left:111px;top:986px;font-size:40px">Trusted House Painters</h2>
<p class="abs body-copy" style="left:113px;top:1038px;width:448px">Are you tired of your current decor and would like to spice it up a bit without burning a hole in your pocket? Well, then our professional and skilled house painters in Auckland City at Tom &amp; Son's Painting have you covered. With a wealth of experience and a knack for perfection, our house painters ensure guaranteed results and spare no efforts in bringing a smile to your face at the end of the service.</p>
<div class="btn" style="left:113px;top:1168px;width:88px;height:29px">Read more</div>

<!-- Reviews -->
<section class="abs reviews"></section>
<h2 class="abs display section-title" style="top:1287px;font-size:40px">Top Reviews</h2>

<svg width="0" height="0" style="position:absolute">
  <defs><symbol id="star" viewBox="0 0 24 24"><polygon points="12,1.5 15,8.6 22.7,9.3 16.9,14.4 18.6,22 12,18 5.4,22 7.1,14.4 1.3,9.3 9,8.6" fill="#f5b800"/></symbol></defs>
</svg>

<article class="abs card" style="left:113px">
  <div class="avatar" role="img" aria-label="Reviewer portrait"></div>
  <div class="reviewer">Hannah Morley</div>
  <svg class="stars" width="84" height="14"><use href="#star" x="0" width="14" height="14"/><use href="#star" x="17" width="14" height="14"/><use href="#star" x="34" width="14" height="14"/><use href="#star" x="51" width="14" height="14"/><use href="#star" x="68" width="14" height="14"/></svg>
  <p class="review-text">Tom and sons painted the exteriorof our home. We are very happy with the timely response in getting the job done, and the thorough final outcome.<br><br>Thanks very much</p>
</article>
<article class="abs card" style="left:443px">
  <div class="avatar" role="img" aria-label="Reviewer portrait"></div>
  <div class="reviewer">Priya Vandenberg</div>
  <svg class="stars" width="84" height="14"><use href="#star" x="0" width="14" height="14"/><use href="#star" x="17" width="14" height="14"/><use href="#star" x="34" width="14" height="14"/><use href="#star" x="51" width="14" height="14"/><use href="#star" x="68" width="14" height="14"/></svg>
  <p class="review-text">Thank you once again for the great job you and your team did for painting our home. We really the colour now! It was nice to meet you all. We wish you all the best and hope you continue to enjoy working and living here in Auckland.</p>
</article>
<article class="abs card" style="left:772px">
  <div class="avatar" role="img" aria-label="Reviewer portrait"></div>
  <div class="reviewer">Sione Tapueluelu</div>
  <svg class="stars" width="84" height="14"><use href="#star" x="0" width="14" height="14"/><use href="#star" x="17" width="14" height="14"/><use href="#star" x="34" width="14" height="14"/><use href="#star" x="51" width="14" height="14"/><use href="#star" x="68" width="14" height="14"/></svg>
  <p class="review-text">We have recently had the interior of our house repainted by Tom and his team. We found them to be very professional and their detail to perfection was top class. We would be pleased to recommend Tom and Sons Painters, at any time and recommend them to others.</p>
</article>
<div class="btn" style="left:531px;top:1590px;width:138px;height:29px">Read all our reviews</div>

<!-- Projects -->
<h2 class="abs display section-title" style="top:1678px;font-size:40px">Our Projects</h2>
<div class="abs pattern-band" role="img" aria-label="Dark green damask wallpaper band"></div>
<article class="abs project" style="left:173px">
  <div class="photo" role="img" aria-label="Bright white living room with grey sofa and potted plant" style="background:linear-gradient(#ececea,#e2e2df 70%,#c9cac8)"></div>
  <h3>Lorem Ipsum</h3>
  <p>Lorem ipsum dolor sit amet, consectetur adipiscing elit.</p>
</article>
<article class="abs project" style="left:610px">
  <div class="photo" role="img" aria-label="Yellow painted room with window, orange chair and bookshelf" style="background:linear-gradient(90deg,#d9b632,#e8c94a 45%,#cfd7c8 55%,#e3c54a 70%,#d8c9a8)"></div>
  <h3>Lorem Ipsum</h3>
  <p>Lorem ipsum dolor sit amet, consectetur adipiscing elit.</p>
</article>
<div class="btn" style="left:531px;top:2128px;width:138px;height:29px">Check all projects</div>

<!-- Newsletter -->
<section class="abs newsletter"></section>
<h2 class="abs display" style="left:185px;top:2234px;font-size:40px;color:#fff">Newsletter</h2>
<p class="abs" style="left:185px;top:2284px;width:400px;font-size:13px;line-height:15px;color:#fff">Subscribe to our newsletter and receive the latest inspiration and design advice, straight to your inbox.</p>
<div class="abs" style="left:719px;top:2241px;width:295px;border-bottom:1px solid rgba(255,255,255,.8);padding-bottom:9px;font-size:12.5px;color:#fff">Enter Your Email</div>
<div class="btn" style="left:719px;top:2284px;width:91px;height:29px;background:#fff;color:var(--green)">Subscribe</div>

<!-- Footer -->
<footer class="abs footer">
  <div class="abs" style="left:213px;top:30px"><h4>NAVIGATE</h4><ul><li>About Us</li><li>Our Services</li><li>Our Projects</li><li>Contact</li></ul></div>
  <div class="abs" style="left:363px;top:30px"><h4>OUR SERVICES</h4><ul><li>Trusted Interior Painting</li><li>Trusted Exterior Painting</li><li>Plastering in Auckland</li></ul></div>
  <div class="abs" style="left:560px;top:30px"><h4>VISIT US</h4><ul><li>14 Fernleaf Lane, Kelston, Auckland.</li><li>brookhollowpaint@mailbox.co.nz</li><li style="font-weight:700">0271458830</li></ul></div>
  <div class="abs" style="left:825px;top:30px"><h4>FOLLOW US</h4></div>
  <span class="footer-dot" style="left:823px" role="img" aria-label="Social profile"></span>
  <span class="footer-dot" style="left:862px" role="img" aria-label="Social profile"></span>
  <span class="footer-dot" style="left:900px" role="img" aria-label="Social profile"></span>
  <div class="abs" style="left:825px;top:89px;width:162px;border-top:1px solid #555"></div>
  <p class="abs" style="left:825px;top:95px;font-size:9.5px">Copyright © 2023 All rights reserved.</p>
</footer>

</body>
</html>
```